Business card design for Automotive workshop

We need a business card for a new automotive repair and tyre shop called Keelstone Prime Automotive located in New Zealand. We are a clean, modern and fresh workshop and company.

Front needs to feature logo,
my name:
Marlo Fitzgerald (director)

Address:
42 Tamsin Road
Marrowby 3742

Phone: 07 541 2298
Mobile: 027 419 5073
Email: office@keelstoneautomotive.co.nz
Website: keelstoneautomotive.co.nz

Back needs to feature an area to write down appointment details, date and time.

Also feature a list of jobs and work we do such as,
Vehicle Servicing
All Mechanical Repairs
Warrant of Fitness
Tyres & Wheel Alignments
Automotive Diagnostics
Automotive Parts & Supplies

```html
<!DOCTYPE html>
<html lang="en">
<head>
<meta charset="utf-8">
<title>Keelstone Prime Automotive – Business Card</title>
<link href="https://fonts.googleapis.com/css2?family=Montserrat:wght@400;500;700&display=swap" rel="stylesheet">
<style>
  :root {
    --backdrop: #e4e2df;
    --card: #2b2b2d;
    --card-deep: #1f1f21;
    --red: #e3222b;
    --white: #f2f2f2;
    --rule: #9a9a9c;
  }
  * { box-sizing: border-box; margin: 0; padding: 0; }
  html, body {
    width: 1200px; height: 900px; overflow: hidden;
    background: var(--backdrop);
    font-family: "Montserrat", sans-serif;
  }
  .canvas {
    width: 1200px; height: 900px;
    display: flex; flex-direction: column; align-items: center; justify-content: center;
    gap: 36px;
  }
  .card {
    position: relative;
    width: 700px; height: 400px;
    background: var(--card);
    color: var(--white);
    box-shadow: 0 12px 30px rgba(0,0,0,.25);
    overflow: hidden;
  }
  .card::after {
    content: ""; position: absolute; left: 0; right: 0; bottom: 0;
    height: 9px; background: var(--red);
  }

  /* Appointment side */
  .appointment .wordmark {
    position: absolute; top: 58px; left: 0; right: 0;
    text-align: center;
    font-weight: 700; font-size: 34px; letter-spacing: 1px;
    color: var(--card-deep);
    text-transform: uppercase;
  }
  .appointment .heading {
    position: absolute; top: 140px; left: 0; right: 0;
    text-align: center; color: var(--red);
    font-weight: 500; font-size: 19px; letter-spacing: .5px;
  }
  .appointment .fields {
    position: absolute; top: 200px; left: 40px; right: 40px;
    display: flex; align-items: flex-end; gap: 8px;
    font-size: 15px;
  }
  .appointment .fill-line {
    flex: 1; border-bottom: 1px solid var(--rule); height: 1px; margin-bottom: 4px;
  }
  .appointment .days {
    position: absolute; top: 280px; left: 150px; right: 40px;
    display: flex; justify-content: space-between;
    list-style: none; font-size: 16px;
  }
  .appointment .days li { display: flex; align-items: center; gap: 8px; }
  .appointment .days li::before {
    content: ""; width: 16px; height: 16px; border-radius: 50%;
    border: 1.5px solid var(--red);
  }

  /* Contact side */
  .contact .wordmark {
    position: absolute; left: 40px; top: 150px; width: 310px;
    font-weight: 700; font-size: 27px; line-height: 1.15;
    color: var(--red); text-transform: uppercase;
  }
  .contact .divider {
    position: absolute; left: 372px; top: 55px; width: 1px; height: 200px;
    background: var(--red);
  }
  .contact .details {
    position: absolute; left: 392px; top: 52px; right: 20px;
    font-size: 14px; line-height: 1.45;
  }
  .contact .name { color: var(--red); font-weight: 700; font-size: 23px; line-height: 1.2; }
  .contact .role { font-size: 15px; margin-bottom: 8px; }
  .contact .address { font-size: 15px; margin-bottom: 8px; }
  .contact .lines { list-style: none; }
  .contact .lines li { display: flex; align-items: center; gap: 7px; }
  .contact .lines svg { width: 12px; height: 12px; flex: none; }
  .contact .services {
    position: absolute; left: 20px; right: 20px; top: 300px;
    text-align: center; font-size: 15px; line-height: 1.6;
  }
  .contact .services .dot { color: var(--red); margin: 0 5px; }
</style>
</head>
<body>
<main class="canvas">

  <section class="card appointment">
    <div class="wordmark">Keelstone Prime Automotive</div>
    <h2 class="heading">APPOINTMENT</h2>
    <div class="fields">
      <span>Date:</span><span class="fill-line"></span>
      <span>Time:</span><span class="fill-line"></span>
    </div>
    <ul class="days">
      <li>Mon</li><li>Tue</li><li>Wed</li><li>Thu</li><li>Fri</li>
    </ul>
  </section>

  <section class="card contact">
    <div class="wordmark">Keelstone Prime Automotive</div>
    <div class="divider"></div>
    <div class="details">
      <div class="name">Marlo Fitzgerald</div>
      <div class="role">director</div>
      <div class="address">42 Tamsin Road<br>Marrowby 3742</div>
      <ul class="lines">
        <li><svg viewBox="0 0 12 12" aria-hidden="true"><path fill="#e3222b" d="M2.5 1 4.5 3.2 3.4 4.6a7 7 0 0 0 4 4L8.8 7.5 11 9.5 9.6 11C5 10.6 1.4 7 1 2.4Z"/></svg>07 541 2298</li>
        <li><svg viewBox="0 0 12 12" aria-hidden="true"><rect x="3" y="0.8" width="6" height="10.4" rx="1" fill="none" stroke="#e3222b" stroke-width="1.2"/><circle cx="6" cy="9.4" r=".7" fill="#e3222b"/></svg>027 419 5073</li>
        <li><svg viewBox="0 0 12 12" aria-hidden="true"><rect x="0.8" y="2.5" width="10.4" height="7" fill="#e3222b"/><path d="M1 3l5 3.5L11 3" fill="none" stroke="#2b2b2d" stroke-width="1"/></svg>office@keelstoneautomotive.co.nz</li>
        <li><svg viewBox="0 0 12 12" aria-hidden="true"><circle cx="6" cy="6" r="5" fill="#e3222b"/><path d="M1 6h10M6 1c-2.5 3-2.5 7 0 10M6 1c2.5 3 2.5 7 0 10" fill="none" stroke="#2b2b2d" stroke-width=".8"/></svg>keelstoneautomotive.co.nz</li>
      </ul>
    </div>
    <p class="services">
      Vehicle Servicing<span class="dot">•</span>All Mechanical Repairs<span class="dot">•</span>Warrant of Fitness<br>
      Tyres &amp; Wheel Alignments<span class="dot">•</span>Automotive Diagnostics<span class="dot">•</span>Automotive Parts &amp; Supplies
    </p>
  </section>

</main>
</body>
</html>
```